Bref créative
Stationery design for KORV Holdings
KORV Holdings - Motion Lessons & Media
Use same font as used in my logo
Trajan Bold
Bright & Fun-filled
Damian Whitcombe
IT & Technical Support
The Lumley House
12 Fenwick Lane
Ashcombe-Under-Lyne
Bristol
BS4 7QD
damian@korv.co
www.korv.co
This is the KORV Holdings logo.

```html
<!DOCTYPE html>
<html lang="en">
<head>
<meta charset="utf-8">
<title>KORV Holdings – Business Card</title>
<link href="https://fonts.googleapis.com/css2?family=Cinzel:wght@700&family=Open+Sans:wght@400;700&display=swap" rel="stylesheet">
<style>
  :root {
    --bg: #d9d9d9;
    --card: #ffffff;
    --card-edge: #f1f1f1;
    --gold: #a8862a;
    --gold-dark: #7a5f12;
    --ink: #3a3a3a;
  }
  * { margin: 0; padding: 0; box-sizing: border-box; }
  html, body { width: 1200px; height: 901px; overflow: hidden; }
  body {
    background: var(--bg);
    position: relative;
    font-family: "Open Sans", Arial, sans-serif;
    color: var(--ink);
  }
  .card {
    position: absolute;
    width: 640px;
    height: 366px;
    border-radius: 22px;
    background: linear-gradient(135deg, var(--card) 0%, var(--card-edge) 100%);
    box-shadow: 0 6px 20px rgba(0,0,0,0.18);
    overflow: hidden;
  }
  .card--back { left: 100px; top: 60px; }
  .card--front { left: 460px; top: 475px; }

  .brand {
    position: absolute;
    font-family: "Cinzel", "Times New Roman", serif;
    font-weight: 700;
    color: var(--gold);
    text-align: center;
    white-space: nowrap;
  }
  .brand-word { display: block; line-height: 1; }
  .brand-sub { display: block; line-height: 1; }

  .card--back .brand { left: 0; right: 0; top: 118px; }
  .card--back .brand-word { font-size: 72px; letter-spacing: 4px; }
  .card--back .brand-sub { font-size: 17px; letter-spacing: 6px; margin-top: 6px; }

  .card--front .brand { left: 34px; top: 26px; }
  .card--front .brand-word { font-size: 56px; letter-spacing: 3px; }
  .card--front .brand-sub { font-size: 14px; letter-spacing: 5px; margin-top: 4px; }

  .address {
    position: absolute;
    left: 34px; top: 118px;
    font-style: normal;
    font-size: 13px;
    line-height: 17px;
    letter-spacing: 1px;
  }
  .contacts {
    position: absolute;
    left: 34px; top: 200px;
    list-style: none;
    font-size: 13px;
    line-height: 19px;
    letter-spacing: 1px;
  }
  .contacts li { display: flex; align-items: center; gap: 8px; }
  .contacts svg { width: 12px; height: 12px; fill: var(--gold); flex: none; }

  .swoosh { position: absolute; inset: 0; width: 640px; height: 366px; }

  .person {
    position: absolute;
    right: 110px; top: 152px;
    text-align: right;
  }
  .person-name { font-size: 15px; font-weight: 700; color: var(--gold-dark); }
  .person-role { font-size: 12px; color: var(--ink); margin-top: 1px; }
</style>
</head>
<body>

  <section class="card card--back">
    <div class="brand">
      <span class="brand-word">KORV</span>
      <span class="brand-sub">HOLDINGS</span>
    </div>
  </section>

  <section class="card card--front">
    <svg class="swoosh" viewBox="0 0 640 366" aria-hidden="true">
      <defs>
        <linearGradient id="goldFill" x1="0" y1="0" x2="1" y2="1">
          <stop offset="0" stop-color="#c9a94a"/>
          <stop offset="0.55" stop-color="#9c7b22"/>
          <stop offset="1" stop-color="#6e540e"/>
        </linearGradient>
      </defs>
      <path d="M640 40 C605 190 480 300 320 366 L640 366 Z" fill="url(#goldFill)"/>
      <path d="M640 215 C575 290 495 335 405 366" fill="none" stroke="#ffffff" stroke-width="5"/>
    </svg>

    <div class="brand">
      <span class="brand-word">KORV</span>
      <span class="brand-sub">HOLDINGS</span>
    </div>

    <address class="address">
      The Lumley House<br>
      12 Fenwick Lane<br>
      Ashcombe-Under-Lyne<br>
      Bristol, BS4 7QD
    </address>

    <ul class="contacts">
      <li><svg viewBox="0 0 12 12"><path d="M2 1h3l1 3-2 1a7 7 0 0 0 3 3l1-2 3 1v3c0 1-1 1-1 1A10 10 0 0 1 1 2c0 0 0-1 1-1z"/></svg>0845 00 12 340</li>
      <li><svg viewBox="0 0 12 12"><path d="M3 0h6a1 1 0 0 1 1 1v10a1 1 0 0 1-1 1H3a1 1 0 0 1-1-1V1a1 1 0 0 1 1-1zm0 2v7h6V2z"/></svg>07700 900 371</li>
      <li><svg viewBox="0 0 12 12"><path d="M3 0h5v3H3zM1 4h10v6H9v2H3v-2H1zm3 4v3h4V8z"/></svg>0845 00 12 440</li>
      <li><svg viewBox="0 0 12 12"><path d="M0 2h12v8H0zm1 1v.5l5 3 5-3V3z"/></svg>damian@korv.co</li>
      <li><svg viewBox="0 0 12 12"><path d="M6 0a6 6 0 1 0 0 12A6 6 0 0 0 6 0zm-1 3 4 3-4 3z"/></svg>www.korv.co</li>
    </ul>

    <div class="person">
      <div class="person-name">Damian Whitcombe</div>
      <div class="person-role">IT &amp; Technical Support</div>
    </div>
  </section>

</body>
</html>
```